New business card design needed for Trucking/Staffing company!

I am looking for a business card design. The business name is Harbor Lane Freightworks, LLC. This company is a staffing company for commercial drivers/truck drivers. Most of our customers are trucking/supply companies. Our colors are blue/black/white/grey. The info I have on my current business cards is
-Spot for a name
-2 lines for an address
-3 lines for Office, cell, and fax
-email
-website(currently on backside of card with logo but can go anywhere)
Updates

Project Deadline Extended
Reason: Open to more designs

Target Market(s)

Trucking companies, building supply companies

Industry/Entity Type

Business

Contact Information for Business Card

Edgy but professional

Font styles to use
Other font styles liked:
• Open to suggestions

Colors
0555a3
000000
ffffff
9d9d9d

Requirements
Must have
• Must have the logo incorporated

```html
<!DOCTYPE html>
<html lang="en">
<head>
<meta charset="utf-8">
<title>Harbor Lane Freightworks – Business Card</title>
<link rel="stylesheet" href="https://fonts.googleapis.com/css2?family=Open+Sans:wght@400;700&display=swap">
<style>
  :root {
    --brand-blue: #0555a3;
    --band-blue: #3f63c4;
    --ink: #000000;
    --paper: #ffffff;
    --grey: #9d9d9d;
    --stage: #e9e9ea;
    --text: #1d1d1d;
  }
  * { box-sizing: border-box; margin: 0; padding: 0; }
  html, body { width: 1200px; height: 892px; overflow: hidden; }
  body {
    background: var(--stage);
    font-family: "Open Sans", Arial, sans-serif;
    color: var(--text);
    display: flex;
    align-items: center;
    justify-content: center;
    gap: 24px;
  }
  .card {
    position: relative;
    width: 560px;
    height: 320px;
    background: var(--paper);
    box-shadow: 0 6px 18px rgba(0,0,0,0.18);
    overflow: hidden;
  }
  /* Front */
  .front-wave { position: absolute; left: 0; bottom: 0; width: 560px; height: 120px; }
  .brand-block {
    position: absolute;
    left: 34px;
    top: 78px;
    width: 200px;
    display: flex;
    align-items: center;
    gap: 10px;
  }
  .brand-mark { width: 14px; height: 14px; background: var(--brand-blue); flex: none; }
  .brand-name {
    font-weight: 700;
    font-size: 19px;
    line-height: 1.15;
    color: var(--brand-blue);
    text-transform: uppercase;
  }
  .divider {
    position: absolute;
    left: 250px;
    top: 28px;
    width: 1px;
    height: 170px;
    background: var(--ink);
  }
  .contact {
    position: absolute;
    left: 274px;
    top: 26px;
    width: 270px;
  }
  .contact-name { font-size: 22px; font-weight: 400; margin-bottom: 10px; color: var(--ink); }
  .contact-address { font-size: 14px; line-height: 1.35; margin-bottom: 10px; }
  .contact-list { list-style: none; font-size: 14px; line-height: 1.55; }
  .contact-list li { display: flex; align-items: center; gap: 8px; }
  .contact-icon { width: 13px; height: 13px; flex: none; }
  /* Back */
  .back { border-top: 14px solid var(--band-blue); border-bottom: 14px solid var(--band-blue); }
  .back-brand {
    position: absolute;
    left: 0; right: 0;
    top: 104px;
    display: flex;
    justify-content: center;
    align-items: center;
    gap: 12px;
  }
  .back-brand .brand-mark { width: 18px; height: 18px; }
  .back-brand .brand-name { font-size: 28px; }
  .website {
    position: absolute;
    left: 0; right: 0;
    top: 178px;
    text-align: center;
    font-size: 16px;
    color: var(--text);
  }
</style>
</head>
<body>

<section class="card front" aria-label="Business card front">
  <svg class="front-wave" viewBox="0 0 560 120" preserveAspectRatio="none" aria-hidden="true">
    <path d="M0,62 C140,62 240,28 330,40 C420,52 480,96 560,84 L560,120 L0,120 Z" fill="var(--ink)"/>
    <path d="M0,74 C140,74 240,40 330,52 C420,64 480,108 560,96 L560,120 L0,120 Z" fill="var(--band-blue)"/>
  </svg>

  <div class="brand-block">
    <span class="brand-mark"></span>
    <span class="brand-name">Harbor Lane Freightworks</span>
  </div>

  <div class="divider"></div>

  <div class="contact">
    <p class="contact-name">Daniel Moreau</p>
    <p class="contact-address">52 Alder Crest Road,<br>8 Wexmoor High Street</p>
    <ul class="contact-list">
      <li>
        <svg class="contact-icon" viewBox="0 0 13 13" aria-label="Office"><rect width="13" height="13" fill="var(--ink)"/><path d="M3.5,3 l1.5,0 l0.7,1.8 l-0.9,0.7 a5,5 0 0 0 2.2,2.2 l0.7,-0.9 l1.8,0.7 l0,1.5 a6.5,6.5 0 0 1 -6,-6z" fill="var(--paper)"/></svg>
        555-210-4837
      </li>
      <li>
        <svg class="contact-icon" viewBox="0 0 13 13" aria-label="Cell"><rect width="13" height="13" fill="var(--ink)"/><rect x="4" y="2.5" width="5" height="8" rx="0.8" fill="var(--paper)"/><rect x="5" y="3.5" width="3" height="5" fill="var(--ink)"/></svg>
        555-318-2604
      </li>
      <li>
        <svg class="contact-icon" viewBox="0 0 13 13" aria-label="Fax"><rect width="13" height="13" fill="var(--ink)"/><rect x="3" y="5" width="7" height="5" fill="var(--paper)"/><rect x="4.5" y="2.5" width="4" height="3" fill="var(--paper)"/></svg>
        555-472-9150
      </li>
      <li>
        <svg class="contact-icon" viewBox="0 0 13 13" aria-label="Email"><rect width="13" height="13" fill="var(--ink)"/><path d="M6.5,2.5 a2.8,2.8 0 0 1 2.8,2.8 c0,2 -2.8,5 -2.8,5 s-2.8,-3 -2.8,-5 a2.8,2.8 0 0 1 2.8,-2.8z" fill="var(--paper)"/><circle cx="6.5" cy="5.3" r="1" fill="var(--ink)"/></svg>
        dmoreau.office@mailbox.com
      </li>
    </ul>
  </div>
</section>

<section class="card back" aria-label="Business card back">
  <div class="back-brand">
    <span class="brand-mark"></span>
    <span class="brand-name">Harbor Lane Freightworks</span>
  </div>
  <p class="website">www.harborlanefreight.com</p>
</section>

</body>
</html>
```